Business card for apparel company. Specializing in fishing and boating performance wear. Main company name is Marlowe Teal Company, LLC brand name for apparel is WAKEFIN. See website www.WakefinReefline.com I will attach some logos to consider.

```html
<!DOCTYPE html>
<html lang="en">
<head>
<meta charset="utf-8">
<title>WAKEFIN Business Card</title>
<link rel="stylesheet" href="https://fonts.googleapis.com/css2?family=Exo+2:wght@800&family=Aldrich&display=swap">
<style>
  :root {
    --backdrop: #979797;
    --card-blue: #0f4e9b;
    --card-blue-glow: #2a62aa;
    --card-white: #ffffff;
    --pattern-tint: #f1f1f3;
    --logo-light: #dcdee4;
    --brand-blue: #1a57a8;
    --accent-cyan: #1fa3e0;
    --contact-grey: #6f6f74;
  }
  * { margin: 0; padding: 0; box-sizing: border-box; }
  html, body { width: 1200px; height: 1000px; overflow: hidden; }
  body { background: var(--backdrop); position: relative; font-family: "Aldrich", sans-serif; }

  .card {
    position: absolute;
    left: 293px;
    width: 615px;
    height: 351px;
    border-radius: 30px;
    overflow: hidden;
  }
  .card--front { top: 104px; background: var(--card-blue); }
  .card--back { top: 504px; background: var(--card-white); }

  .front-decor {
    position: absolute;
    right: 0; top: 0;
    width: 340px; height: 351px;
    background: radial-gradient(ellipse at 65% 55%, var(--card-blue-glow) 0%, rgba(42,98,170,0.35) 45%, rgba(15,78,155,0) 75%);
  }
  .back-decor {
    position: absolute; inset: 0;
    background: linear-gradient(160deg, var(--pattern-tint) 0%, #fbfbfc 55%, var(--pattern-tint) 100%);
  }

  .brand-name {
    font-family: "Exo 2", sans-serif;
    font-weight: 800;
    font-size: 32px;
    letter-spacing: 2px;
    line-height: 32px;
  }
  .brand-tagline {
    font-family: "Exo 2", sans-serif;
    font-weight: 800;
    font-size: 20px;
    letter-spacing: 2px;
    line-height: 20px;
  }

  .front-brand {
    position: absolute;
    left: 0; top: 171px;
    width: 375px;
    text-align: center;
    color: var(--logo-light);
  }
  .front-brand .brand-tagline { margin-top: 6px; color: #ffffff; }
  .front-web {
    position: absolute;
    left: 0; top: 246px;
    width: 365px;
    text-align: center;
    font-size: 15px;
    line-height: 16px;
    letter-spacing: 0.6px;
    color: var(--accent-cyan);
  }

  .back-brand {
    position: absolute;
    left: 0; top: 158px;
    width: 615px;
    text-align: center;
    color: var(--brand-blue);
  }
  .back-brand .brand-tagline { margin-top: 3px; }

  .contact-list {
    position: absolute;
    left: 0; top: 239px;
    width: 615px;
    list-style: none;
    text-align: center;
    color: var(--contact-grey);
    font-size: 14px;
    letter-spacing: 1.2px;
  }
  .contact-list li { height: 22px; display: flex; justify-content: center; align-items: center; gap: 6px; }
  .contact-list svg { fill: var(--accent-cyan); }

  .location {
    position: absolute;
    left: 0; top: 309px;
    width: 615px;
    display: flex;
    justify-content: center;
    align-items: center;
    gap: 8px;
    color: var(--brand-blue);
    font-size: 13px;
    letter-spacing: 1.5px;
  }
  .location-rule { width: 74px; height: 3px; }
</style>
</head>
<body>
  <section class="card card--front">
    <div class="front-decor" role="img" aria-label="Large faint brand symbol watermark"></div>
    <div class="front-brand">
      <div class="brand-name">WAKEFIN</div>
      <div class="brand-tagline">SALT RIDGE LOCAL</div>
    </div>
    <div class="front-web">WAKEFINREEFLINE.COM</div>
  </section>

  <section class="card card--back">
    <div class="back-decor" role="img" aria-label="Faint repeating brand symbol pattern"></div>
    <div class="back-brand">
      <div class="brand-name">WAKEFIN</div>
      <div class="brand-tagline">SALT RIDGE LOCAL</div>
    </div>
    <ul class="contact-list">
      <li>
        <svg width="14" height="14" viewBox="0 0 24 24" aria-hidden="true"><path d="M6.6 10.8a15.1 15.1 0 0 0 6.6 6.6l2.2-2.2c.3-.3.7-.4 1-.2 1.1.4 2.3.6 3.6.6.6 0 1 .4 1 1V20c0 .6-.4 1-1 1A17 17 0 0 1 3 4c0-.6.4-1 1-1h3.5c.6 0 1 .4 1 1 0 1.3.2 2.5.6 3.6.1.3 0 .7-.2 1l-2.3 2.2z"/></svg>
        <span>012-345-678</span>
      </li>
      <li>
        <svg width="16" height="12" viewBox="0 0 16 12" aria-hidden="true"><path d="M0 0h16v12H0z"/><path d="M1 1.5 8 7.2l7-5.7" fill="none" stroke="#fff" stroke-width="1"/></svg>
        <span>INFO@MARLOWETEALCO.COM</span>
      </li>
    </ul>
    <div class="location">
      <svg class="location-rule" viewBox="0 0 74 3" aria-hidden="true"><path d="M0 1.5 L74 0 L74 3 Z" fill="var(--brand-blue)"/></svg>
      <span>BAYHAVEN, FL</span>
      <svg class="location-rule" viewBox="0 0 74 3" aria-hidden="true"><path d="M74 1.5 L0 0 L0 3 Z" fill="var(--brand-blue)"/></svg>
    </div>
  </section>
</body>
</html>
```